Bright Fern Custom Homes business card. Double sided. Modern. professional

Bright Fern Custom Homes
contemporary modern design with our logo /
Double sided with all our contact information
Use same Green colors as in our Logo. Contemporary logo that grabs your attention. Visually pleasing and balanced. Easy to read, and Vibrant. Would love an option for rounded edges. Embossed logo would be amazing.
Contact Information for Business Card
Dana Welk Owner / General Contractor Bright Fern Custom Homes p: 704.552.1830 m: 912.648.2071 e: brightferncustomhomes@mailbox.example w: www.brightferncustomhomes.example 218 Pryor Meadow Lane Batesburg, SC 29041

```html
<!DOCTYPE html>
<html lang="en">
<head>
<meta charset="utf-8">
<title>Bright Fern Custom Homes – Business Card</title>
<link rel="stylesheet" href="https://fonts.googleapis.com/css2?family=Open+Sans:wght@400;600;700&display=swap">
<style>
  :root {
    --bg: #b9b9b9;
    --card-white: #ffffff;
    --card-black: #050608;
    --fern: #6b8a2e;
    --fern-dark: #5a7724;
    --rule: #8ea44f;
  }
  * { box-sizing: border-box; margin: 0; padding: 0; }
  html, body {
    width: 1200px; height: 848px; overflow: hidden;
    background: var(--bg);
    font-family: "Open Sans", Arial, sans-serif;
  }
  .sheet {
    width: 1200px; height: 848px;
    display: flex; align-items: center; justify-content: center; gap: 40px;
  }
  .card {
    position: relative;
    width: 540px; height: 309px;
    border-radius: 34px;
    overflow: hidden;
  }
  .card--front { background: var(--card-white); }
  .card--back { background: var(--card-black); }

  .brand {
    color: var(--fern);
    font-weight: 600;
    text-transform: uppercase;
    letter-spacing: 0.14em;
    text-align: center;
    line-height: 1.25;
  }
  .brand__mark {
    width: 14px; height: 14px; border-radius: 50%;
    background: var(--fern); display: block; margin: 0 auto 10px;
  }
  .brand__sub { display: block; }

  /* front */
  .front__brand {
    position: absolute; left: 40px; top: 56px; width: 300px;
    font-size: 24px;
  }
  .front__brand .brand__sub { font-size: 11px; letter-spacing: 0.5em; margin-top: 6px; }
  .contact-list {
    position: absolute; left: 14px; top: 176px; width: 332px;
    list-style: none;
  }
  .contact-list li {
    display: flex; align-items: center; justify-content: flex-end; gap: 8px;
    color: var(--fern); font-size: 12.5px; line-height: 24px; white-space: nowrap;
  }
  .icon { width: 14px; height: 14px; flex: none; fill: var(--fern); }
  .divider {
    position: absolute; left: 360px; top: 150px; width: 1px; height: 112px;
    background: var(--rule);
  }
  .person {
    position: absolute; left: 376px; top: 150px;
    color: var(--fern);
  }
  .person__name { font-weight: 700; font-size: 13px; text-transform: uppercase; letter-spacing: 0.02em; }
  .person__role { font-size: 12px; text-transform: uppercase; margin-bottom: 10px; }
  .person__phone { display: flex; align-items: center; gap: 8px; font-size: 13px; line-height: 24px; }

  /* back */
  .back__brand {
    position: absolute; left: 0; right: 0; top: 106px;
    font-size: 28px;
  }
  .back__brand .brand__name { color: var(--fern-dark); }
  .back__brand .brand__sub { font-size: 12px; letter-spacing: 0.55em; margin-top: 8px; color: var(--fern-dark); }
</style>
</head>
<body>
<main class="sheet">
  <section class="card card--front" aria-label="Business card front">
    <div class="brand front__brand">
      <span class="brand__mark"></span>
      <span class="brand__name">Bright Fern</span>
      <span class="brand__sub">Custom Homes</span>
    </div>

    <ul class="contact-list">
      <li>brightferncustomhomes@mailbox.example
        <svg class="icon" viewBox="0 0 16 16" aria-hidden="true"><path d="M1 3h14v10H1z M2 4.2v.6l6 4 6-4v-.6z" fill-rule="evenodd"/></svg>
      </li>
      <li>www.brightferncustomhomes.example
        <svg class="icon" viewBox="0 0 16 16" aria-hidden="true"><circle cx="8" cy="8" r="6.5" fill="none" stroke="#6b8a2e" stroke-width="1.2"/><ellipse cx="8" cy="8" rx="2.8" ry="6.5" fill="none" stroke="#6b8a2e" stroke-width="1.2"/><path d="M1.5 8h13M2.5 5h11M2.5 11h11" stroke="#6b8a2e" stroke-width="1"/></svg>
      </li>
      <li>218 Pryor Meadow Lane Alder Falls, SC 29041
        <svg class="icon" viewBox="0 0 16 16" aria-hidden="true"><path d="M8 1a5 5 0 0 1 5 5c0 3.5-5 9-5 9S3 9.5 3 6a5 5 0 0 1 5-5zm0 3a2 2 0 1 0 0 4 2 2 0 0 0 0-4z" fill-rule="evenodd"/></svg>
      </li>
    </ul>

    <div class="divider"></div>

    <div class="person">
      <p class="person__name">Dana Welk / Owner</p>
      <p class="person__role">General Contractor</p>
      <p class="person__phone">
        <svg class="icon" viewBox="0 0 16 16" aria-hidden="true"><path d="M3.5 1.5l2.5 0 1 3.5-1.6 1.2a8 8 0 0 0 4.4 4.4L11 9l3.5 1v2.5c0 1-1 2-2 2C6.5 14.5 1.5 9.5 1.5 3.5c0-1 1-2 2-2z"/></svg>
        704.552.1830
      </p>
      <p class="person__phone">
        <svg class="icon" viewBox="0 0 16 16" aria-hidden="true"><path d="M4.5 1h7a1 1 0 0 1 1 1v12a1 1 0 0 1-1 1h-7a1 1 0 0 1-1-1V2a1 1 0 0 1 1-1zm.5 2v9h6V3z" fill-rule="evenodd"/></svg>
        912.648.2071
      </p>
    </div>
  </section>

  <section class="card card--back" aria-label="Business card back">
    <div class="brand back__brand">
      <span class="brand__mark"></span>
      <span class="brand__name">Bright Fern</span>
      <span class="brand__sub">Custom Homes</span>
    </div>
  </section>
</main>
</body>
</html>
```